Social

We are seeking a skilled designer to create a set of visually compelling social media ad creatives that will drive traffic to our Wood Look Paver landing page, encouraging visitors to download our brochure.
Landing page: https://stonevelmo.com/wood-look-porcelain-paver-solutions-downloadable-guide/
The broader campaign is focused on educating architects, contractors, and homeowners on the availability and advantages of wood look porcelain pavers as an alternative to natural wood. Ads will highlight both real-world installation images and available wood sample colors to spark interest and drive click-throughs.
Scope:
Design 3 ad sets with distinct styling and copy concepts.
Ads should align with platform best practices for:
Facebook
Instagram
LinkedIn
See brief for sizing.
Creative Direction:
Use installation photos and wood sample color swatches as primary visuals.
Design should clearly highlight the brochure download call-to-action.
Visual style should balance modern and professional, appealing to both design professionals and homeowners.
Target Market(s)
Architects
Industry/Entity Type
Construction
Font styles to use
Other font styles liked:
- Outfit, Helvetica (other fonts are possible)
Look and feel
Each slider illustrates characteristics of the customer's brand and the style your logo design should communicate.

```html
<!DOCTYPE html>
<html lang="en">
<head>
<meta charset="utf-8">
<title>Stonevelmo – Ad set 1</title>
<link href="https://fonts.googleapis.com/css2?family=Outfit:wght@200;300;400;500;600&family=Roboto:wght@300;400&family=Great+Vibes&display=swap" rel="stylesheet">
<style>
  :root{
    --ink:#1d1d1d;
    --white:#ffffff;
    --teal:#0d7a86;
    --teal-deep:#0a5f66;
    --teal-green:#0c6b5c;
    --gold:#f3d21a;
    --gold-line:#e6c94a;
    --wood:#b98c63;
    --wood-light:#d8bd9c;
    --slate:#3b3f42;
    --muted:#555;
  }
  *{box-sizing:border-box;margin:0;padding:0}
  html,body{width:1200px;height:467px;overflow:hidden;background:var(--white)}
  body{position:relative;font-family:"Outfit",sans-serif;color:var(--ink)}

  .set-title{position:absolute;left:512px;top:0;width:184px;height:35px;background:var(--ink);color:var(--white);
    font-weight:300;font-size:23px;display:flex;align-items:center;justify-content:center;letter-spacing:.3px}
  .size-label{position:absolute;top:64px;font-family:"Roboto",sans-serif;font-size:11px;color:var(--ink);transform:translateX(-50%)}

  .ad{position:absolute;top:93px;width:332px;height:332px;overflow:hidden;box-shadow:0 2px 10px rgba(0,0,0,.18)}
  .ad-1{left:55px;background:var(--white)}
  .ad-2{left:438px}
  .ad-3{left:816px}
  .abs{position:absolute}

  .brand{position:absolute;display:flex;align-items:center;gap:6px;font-weight:400;font-size:23px;line-height:1;letter-spacing:.2px}
  .brand-mark{width:15px;height:15px;display:block}
  .dots{position:absolute;width:54px;height:18px;
    background-image:radial-gradient(circle,#b9b9b9 .7px,transparent 1px);background-size:6px 6px}

  .cta{position:absolute;background:var(--gold);color:var(--ink);font-size:7.5px;font-weight:400;
    display:flex;align-items:center;justify-content:center}

  /* Ad 1 */
  .ad-1 .band{left:0;top:182px;width:332px;height:150px;background:linear-gradient(180deg,var(--teal-deep),var(--teal-green) 70%,#0e7a5e)}
  .ad-1 .brand{left:26px;top:18px;color:var(--ink)}
  .ad-1 .dots{left:222px;top:20px}
  .ad-1 .photo-frame{left:26px;top:52px;width:143px;height:212px;background:#1a1a1a}
  .ad-1 .photo{left:32px;top:58px;width:156px;height:212px;background:linear-gradient(180deg,#4d6a3a 0%,#7c8a66 35%,#c9ab86 60%,var(--wood) 100%)}
  .ad-1 .rule-v{left:198px;top:71px;width:1px;height:211px;background:var(--gold-line)}
  .ad-1 .rule-h{left:127px;top:282px;width:72px;height:1px;background:var(--gold-line)}
  .ad-1 .headline{left:206px;top:74px;color:var(--teal);font-size:26px;line-height:23.5px}
  .ad-1 .headline .b{font-weight:500}
  .ad-1 .headline .l{font-weight:200}
  .ad-1 .body{left:208px;top:204px;color:var(--white);font-family:"Roboto",sans-serif;font-weight:300;font-size:13.5px;line-height:15.6px}
  .ad-1 .cta{left:32px;top:291px;width:78px;height:18px}

  /* Ad 2 */
  .ad-2 .bg{inset:0;background:linear-gradient(100deg,var(--teal) 0%,var(--teal) 38%,rgba(13,122,134,.75) 55%,#8a7460 80%,var(--wood) 100%)}
  .ad-2 .sky{right:0;top:0;width:150px;height:90px;background:linear-gradient(200deg,#e8eff0,rgba(200,220,222,0))}
  .ad-2 .brand{left:38px;top:20px;color:var(--white)}
  .ad-2 .dots{left:260px;top:24px;background-image:radial-gradient(circle,rgba(255,255,255,.45) .7px,transparent 1px)}
  .ad-2 .frame-top{left:24px;top:54px;width:219px;height:1px;background:var(--gold-line)}
  .ad-2 .frame-left{left:24px;top:54px;width:1px;height:143px;background:var(--gold-line)}
  .ad-2 .frame-right{left:307px;top:169px;width:1px;height:141px;background:var(--gold-line)}
  .ad-2 .frame-bottom{left:234px;top:310px;width:74px;height:1px;background:var(--gold-line)}
  .ad-2 .headline{left:38px;top:65px;color:var(--white);font-size:23px;line-height:23.5px}
  .ad-2 .headline .b{font-weight:500}
  .ad-2 .headline .l{font-weight:200}
  .ad-2 .count{left:40px;top:147px;color:var(--white);font-size:38px;font-weight:400;line-height:1}
  .ad-2 .count-script{left:42px;top:174px;color:var(--gold);font-family:"Great Vibes",cursive;font-size:25px;line-height:1}
  .ad-2 .swatch{border-radius:2px;box-shadow:0 1px 3px rgba(0,0,0,.3)}
  .sw-grey{left:135px;top:145px;width:57px;height:42px;background:linear-gradient(90deg,#6e6a66,#8d8984,#6a6560)}
  .sw-walnut{left:201px;top:145px;width:57px;height:71px;background:linear-gradient(90deg,#8a5a3b,#a26e4b,#8c5c3d)}
  .sw-oak{left:135px;top:196px;width:57px;height:72px;background:linear-gradient(90deg,#c99c62,#dcb07a,#c8985c)}
  .sw-ash{left:201px;top:225px;width:57px;height:43px;background:linear-gradient(90deg,#d6d0c6,#e6e1d8,#d2cbc0)}
  .ad-2 .body{left:38px;top:210px;color:var(--white);font-family:"Roboto",sans-serif;font-weight:300;font-size:12.5px;line-height:15.5px}
  .ad-2 .cta{left:40px;top:291px;width:78px;height:18px}

  /* Ad 3 */
  .ad-3 .bg{inset:0;background:linear-gradient(160deg,#7d7b77 0%,#d9d7d2 30%,#a58a6c 70%,#8d6a4b 100%)}
  .ad-3 .brand{left:180px;top:18px;color:var(--ink)}
  .ad-3 .brand-rule{left:180px;top:46px;width:152px;height:1px;background:var(--gold-line)}
  .ad-3 .panel{left:68px;top:62px;width:264px;height:212px;background:linear-gradient(180deg,#0a0a0a 0%,#2e2f30 55%,#6e6d6a 100%)}
  .ad-3 .headline{right:15px;top:70px;text-align:right;color:var(--white);font-size:25px;line-height:26px}
  .ad-3 .headline .b{font-weight:500}
  .ad-3 .headline .l{font-weight:200}
  .ad-3 .sub{right:15px;top:126px;text-align:right;color:var(--white);font-family:"Roboto",sans-serif;font-size:12px;line-height:14px}
  .ad-3 .footer{left:0;top:274px;width:320px;height:58px;background:linear-gradient(90deg,rgba(255,255,255,.55),rgba(255,255,255,.92) 45%)}
  .ad-3 .edge{left:320px;top:274px;width:12px;height:58px;background:var(--ink)}
  .ad-3 .footer-rule{left:141px;top:283px;width:179px;height:1px;background:var(--gold-line)}
  .ad-3 .shield{left:106px;top:295px;width:22px;height:23px}
  .ad-3 .note{left:131px;top:295px;color:var(--muted);font-size:10.5px;line-height:11px;font-weight:300}
  .ad-3 .cta{left:226px;top:296px;width:77px;height:18px}
</style>
</head>
<body>
  <div class="set-title">Ad set-1</div>
  <div class="size-label" style="left:216px">1440x1440</div>
  <div class="size-label" style="left:605px">1440x1440</div>
  <div class="size-label" style="left:977px">1440x1440</div>

  <!-- Ad 1 -->
  <section class="ad ad-1">
    <div class="abs band" role="img" aria-label="Garden greenery and wood-look porcelain deck in teal tones"></div>
    <div class="brand"><svg class="brand-mark" viewBox="0 0 15 15"><rect width="15" height="15" fill="var(--teal)"/></svg>Stonevelmo</div>
    <div class="dots"></div>
    <div class="abs photo-frame"></div>
    <div class="abs photo" role="img" aria-label="Modern terrace with wood-look porcelain pavers beside a garden"></div>
    <div class="abs rule-v"></div>
    <div class="abs rule-h"></div>
    <h2 class="abs headline"><span class="b">Wood</span><br><span class="l">Look</span><br><span class="b">Porcelain</span><br><span class="l">Pavers</span></h2>
    <p class="abs body">The warmth of<br>natural wood,<br>the advantages<br>of porcelain</p>
    <a class="cta">Download the Guide</a>
  </section>

  <!-- Ad 2 -->
  <section class="ad ad-2">
    <div class="abs bg" role="img" aria-label="Covered outdoor terrace with wood-look porcelain planks"></div>
    <div class="abs sky"></div>
    <div class="brand"><svg class="brand-mark" viewBox="0 0 15 15"><rect width="15" height="15" fill="var(--white)"/></svg>Stonevelmo</div>
    <div class="dots"></div>
    <div class="abs frame-top"></div>
    <div class="abs frame-left"></div>
    <div class="abs frame-right"></div>
    <div class="abs frame-bottom"></div>
    <h2 class="abs headline"><span class="b">Wood Look</span><br><span class="l">Porcelain</span><br><span class="b">Pavers</span> <span class="l">and</span> <span class="b">Planks</span></h2>
    <div class="abs count">20+</div>
    <div class="abs count-script">styles</div>
    <div class="abs swatch sw-grey" role="img" aria-label="Grey weathered wood swatch"></div>
    <div class="abs swatch sw-walnut" role="img" aria-label="Walnut wood swatch"></div>
    <div class="abs swatch sw-oak" role="img" aria-label="Honey oak wood swatch"></div>
    <div class="abs swatch sw-ash" role="img" aria-label="Pale ash wood swatch"></div>
    <p class="abs body">The rich details<br>of wood, the<br>advantages of<br>porcelain</p>
    <a class="cta">Order a Sample</a>
  </section>

  <!-- Ad 3 -->
  <section class="ad ad-3">
    <div class="abs bg" role="img" aria-label="Rooftop deck with wood-look porcelain pavers and glass facade"></div>
    <div class="brand"><svg class="brand-mark" viewBox="0 0 15 15"><rect width="15" height="15" fill="var(--teal)"/></svg>Stonevelmo</div>
    <div class="abs brand-rule"></div>
    <div class="abs panel" role="img" aria-label="Steel pedestals supporting an elevated deck"></div>
    <h2 class="abs headline"><span class="b">Build 100%</span><br><span class="l">Fireproof Decks</span></h2>
    <p class="abs sub">On-grade or elevated on<br>steel pedestals</p>
    <div class="abs footer"></div>
    <div class="abs edge"></div>
    <div class="abs footer-rule"></div>
    <svg class="abs shield" viewBox="0 0 22 23" fill="none" stroke="var(--teal)" stroke-width="1.4">
      <path d="M11 1.5 L19.5 5 V11 C19.5 16 15.5 19.5 11 21.5 C6.5 19.5 2.5 16 2.5 11 V5 Z"/>
      <path d="M12 16 C9.5 15 10 12 12 10 C12 12 14.5 12.5 14 15 C13.7 16 12.8 16.3 12 16 Z"/>
    </svg>
    <p class="abs note">Class A fire rated<br>decking system.</p>
    <a class="cta">Learn More</a>
  </section>
</body>
</html>
```